Study report design for interngovernmental organisation

We need a designer to provide a cover (front and back) to a prosaic governmental report. We need an introduction page, and just numbers and chapter designs throughout also. We would need the design in word format as we're incapable of working with anything else, and we still have a lot to edit! The topic is illicit financial flows, so ideas that come to mind: briefcases with money, anything that depicts money travelling across borders in an illicit manner.

Target Market(s)

Governments

Font styles to use
Serif
Sans Serif

Requirements
Must have
• A sober feel. Nothing too extravagant!

```html
<!DOCTYPE html>
<html lang="en">
<head>
<meta charset="utf-8">
<title>Study Report – Executive Summary Spread</title>
<link rel="stylesheet" href="https://fonts.googleapis.com/css2?family=Open+Sans:wght@400;600;700&display=swap">
<style>
  :root {
    --ink: #3a3d42;
    --ink-strong: #23262b;
    --brand-blue: #1f64b4;
    --band-dark: #2b2d31;
    --page-white: #ffffff;
    --backdrop: #e6e7e9;
    --photo-light: #dbe3ec;
    --photo-mid: #9fb0c2;
    --photo-dark: #2e3137;
  }
  * { box-sizing: border-box; margin: 0; padding: 0; }
  html, body {
    width: 1200px; height: 831px; overflow: hidden;
    background: var(--backdrop);
    font-family: "Open Sans", Arial, sans-serif;
  }
  .spread { display: flex; width: 1200px; height: 831px; }
  .page { position: relative; width: 600px; height: 831px; background: var(--page-white); overflow: hidden; }

  .page--portrait .portrait-photo {
    position: absolute; inset: 0;
    background:
      linear-gradient(90deg, rgba(219,227,236,0.9) 0%, rgba(219,227,236,0) 18%, rgba(219,227,236,0) 82%, rgba(200,210,222,0.9) 100%),
      linear-gradient(180deg, var(--photo-light) 0%, var(--photo-mid) 38%, var(--photo-dark) 60%, var(--photo-dark) 100%);
  }

  .page--summary { padding: 50px 52px 0 54px; color: var(--ink); }
  .summary-title {
    font-size: 27px; font-weight: 600; color: var(--brand-blue);
    letter-spacing: 0.2px; margin-bottom: 6px;
  }
  .summary-text p { font-size: 11.2px; line-height: 1.4; margin-bottom: 11px; }
  .summary-text strong { color: var(--ink-strong); font-weight: 700; }
  .lead { font-weight: 700; color: var(--ink-strong); margin-bottom: 8px !important; }
  .section-heading {
    font-size: 13px; font-weight: 600; color: var(--brand-blue); margin: 14px 0 9px;
  }
  .method-list { list-style: none; margin: 6px 0 12px; }
  .method-list li {
    position: relative; padding-left: 24px; font-size: 11.2px; line-height: 1.4; margin-bottom: 9px;
  }
  .method-list li::before {
    content: ""; position: absolute; left: 6px; top: 6px;
    width: 6px; height: 6px; border-radius: 50%; background: var(--brand-blue);
  }

  .page-number {
    position: absolute; right: 26px; top: 708px;
    font-size: 10px; color: var(--ink);
  }
  .footer-bands { position: absolute; left: 0; bottom: 0; width: 600px; height: 110px; }
</style>
</head>
<body>
  <main class="spread">
    <section class="page page--portrait">
      <div class="portrait-photo" role="img" aria-label="Portrait photograph of a businessman in a dark pinstripe suit with arms crossed, against a pale blue office backdrop"></div>
    </section>

    <section class="page page--summary">
      <h1 class="summary-title">Executive Summary</h1>
      <div class="summary-text">
        <p class="lead">This Study report responds to the request from the G-Forum Leaders’ Communiqué September 2016 for the ICTO:</p>
        <p>“We will continue our work on addressing cross-border financial flows derived from illicit activities, including deliberate trade misinvoicing, which hampers the mobilization of domestic resources for development, and welcome the communication and coordination with the International Customs and Trade Organization for a study report in this regard following the Lakeside Summit.” (paragraph 36)</p>
        <p><strong>The report has been prepared in collaboration</strong> between experts and scholars from the ICTO, CEDA, FFI, academia and Customs administrations, under the responsibility of the Secretariat of the ICTO. However, the report should not be regarded as the officially endorsed views of those organizations or of their member countries.</p>
        <p><strong>The request from the G-Forum arises in the context of increased concern about Illicit Financial Flows (IFFs) channeled via trade mis-invoicing (TM).</strong> Empirical research revealed significantly high estimates of IFFs via TM (IFFs/TM). In particular, the Meridian Expert Commission on Cross-Border Revenue Loss (2015) argued that Africa lost over 50 billion USD annually from illicit financial outflows, which exceed levels of Official Development Assistance to the continent.</p>
        <p><strong>In that context, the report 1) examines whether such high estimates of IFFs/TM are reliable, and 2) presents policy recommendations summarized from the best practices of Customs administrations to tackle IFFs/TM.</strong></p>

        <h2 class="section-heading">1) Estimates of IFFs/TM</h2>
        <p>Empirical research employed either of the following methods to estimate the magnitude of IFFs/TM;</p>
        <ul class="method-list">
          <li>Partner Country Method (known as mirror data analysis), which measures discrepancies in bilateral trade records between trade partners; and</li>
          <li>Price Filter Method (known as unit price analysis), which measures the mis-invoiced value of trade transactions for which the unit price is considered abnormal.</li>
        </ul>
        <p><strong>The report suggests that estimates of IFFs/TM are not sufficiently robust</strong> across the two methods. Even estimates from the same method with the same trade data ranged widely according to the different assumptions. Therefore, the high estimates of IFFs/TM which feature prominently in current literature, research and even media outlets, should not be understood as a reliable quantitative measurement of the scale of IFFs/TM, but rather as a risk indicator, which can be useful in comparing the risk of IFFs/TM across commodities, countries and over a longer time period.</p>
      </div>

      <span class="page-number">7</span>
      <svg class="footer-bands" viewBox="0 0 600 110" aria-hidden="true">
        <polygon points="0,78 600,50 600,66 0,104" fill="var(--band-dark)"/>
        <polygon points="488,62 600,54 600,66 480,74" fill="var(--page-white)"/>
        <polygon points="498,38 600,32 600,64 488,70" fill="var(--brand-blue)"/>
      </svg>
    </section>
  </main>
</body>
</html>
```